Communications & Broadcast Consulting/PR/Media Relations & Public Affairs

My main goals are to provide communications support to school districts, small towns/cities/hospitals and private businesses in the form of press releases, media relations, public affairs. I also have 25 years experience as a television news anchor/reporter and I'm open to free-lance reporting in both Indianapolis and other markets. My specialty is working with the media.
Communications

```html
<!DOCTYPE html>
<html lang="en">
<head>
<meta charset="utf-8">
<title>Ridgeline Communications – Business Card</title>
<link href="https://fonts.googleapis.com/css2?family=Open+Sans:wght@400&display=swap" rel="stylesheet">
<style>
  :root {
    --backdrop: #d5d5d7;
    --card: #fbfbfb;
    --frame: #111111;
    --rule: #8a8a8a;
    --ink: #1e1e1e;
    --accent: #2bb24c;
  }
  * { margin: 0; padding: 0; box-sizing: border-box; }
  html, body {
    width: 883px; height: 1200px; overflow: hidden;
    background: var(--backdrop);
    font-family: "Open Sans", Arial, sans-serif;
    color: var(--ink);
  }
  .stage { position: relative; width: 883px; height: 1200px; }
  .card {
    position: absolute; left: 247px; width: 389px; height: 218px;
    background: var(--card);
    box-shadow: 0 1px 3px rgba(0,0,0,.18);
  }
  .card--front { top: 380px; }
  .card--back { top: 620px; }
  .card__frame {
    position: absolute; left: 18px; top: 16px; right: 17px; bottom: 16px;
    border: 2px solid var(--frame);
  }
  .wordmark {
    position: absolute; text-align: center; color: var(--ink);
    font-weight: 400; line-height: 1.1;
  }
  .wordmark__name { display: block; font-size: 29px; letter-spacing: .5px; }
  .wordmark__sub { display: block; font-size: 14px; letter-spacing: 1.2px; }
  .card--front .wordmark { left: 0; right: 0; top: 80px; }
  .card--back .wordmark { right: 28px; top: 50px; }
  .card--back .wordmark__name { font-size: 24px; }
  .card--back .wordmark__sub { font-size: 12px; }
  .band-rule {
    position: absolute; left: 0; right: 0; height: 1px; background: var(--rule);
  }
  .band-rule--top { top: 118px; }
  .band-rule--bottom { top: 136px; }
  .identity {
    position: absolute; left: 29px; top: 117px;
    display: flex; align-items: baseline; color: var(--accent);
  }
  .identity__name { font-size: 15px; }
  .identity__role {
    font-size: 11px; margin-left: 6px; padding-left: 6px;
    border-left: 1px solid var(--accent);
  }
  .contacts { position: absolute; left: 30px; top: 146px; list-style: none; }
  .contacts li {
    display: flex; align-items: center; font-size: 10.5px; height: 12.5px;
  }
  .contacts svg { width: 9px; height: 9px; margin-right: 8px; fill: var(--ink); }
</style>
</head>
<body>
<main class="stage">
  <section class="card card--front" aria-label="Card front">
    <div class="card__frame"></div>
    <div class="wordmark">
      <span class="wordmark__name">Ridgeline</span>
      <span class="wordmark__sub">Communications</span>
    </div>
  </section>

  <section class="card card--back" aria-label="Card back">
    <div class="card__frame"></div>
    <div class="wordmark">
      <span class="wordmark__name">Ridgeline</span>
      <span class="wordmark__sub">Communications</span>
    </div>
    <div class="band-rule band-rule--top"></div>
    <div class="band-rule band-rule--bottom"></div>
    <div class="identity">
      <span class="identity__name">your name</span>
      <span class="identity__role">designation</span>
    </div>
    <ul class="contacts">
      <li><svg viewBox="0 0 10 10" aria-hidden="true"><path d="M1 3q4-3 8 0v2H7V4H3v1H1zM2 6h6l1 3H1z"/></svg>IN 46000 555.210.4477</li>
      <li><svg viewBox="0 0 10 10" aria-hidden="true"><path d="M3 0h4a1 1 0 0 1 1 1v8a1 1 0 0 1-1 1H3a1 1 0 0 1-1-1V1a1 1 0 0 1 1-1zm0 1v7h4V1z"/></svg>555.304.6182</li>
      <li><svg viewBox="0 0 10 10" aria-hidden="true"><path d="M0 2h10v6H0zM1 3l4 3 4-3z" fill-rule="evenodd"/></svg>rridgeline12@mailbox.com</li>
      <li><svg viewBox="0 0 10 10" aria-hidden="true"><path d="M5 0a3.5 3.5 0 0 1 3.5 3.5C8.5 6 5 10 5 10S1.5 6 1.5 3.5A3.5 3.5 0 0 1 5 0zm0 2a1.5 1.5 0 1 0 0 3 1.5 1.5 0 0 0 0-3z"/></svg>2818 Maple Grove Lane Springfield</li>
    </ul>
  </section>
</main>
</body>
</html>
```